Marbella Specialty Coffee needs a Packaging design

We need packaging design for coffee that suits our brand identity, that is the best quality in Mexico.
We only sell mexican coffee with Q scores above 80
We are evaluating 3 types of packaging: Bag, Box and Cillinder can
The specific package format will be decided based on the designs that we get.

Target Market(s)

Coffee experts and enthusiast.
People that relate the Coffee consumption and experience with wine tasting and Bon Vivant way

Requirements
Should not have
• Photos any mexican cliché

```html
<!DOCTYPE html>
<html lang="en">
<head>
<meta charset="utf-8">
<title>Marbella Specialty Coffee – Mexican Roast Ground</title>
<link rel="stylesheet" href="https://fonts.googleapis.com/css2?family=Fira+Sans:wght@400;600;700&family=Merienda:wght@400&display=swap">
<style>
  :root {
    --backdrop: #2a1a12;
    --pack-black: #050505;
    --band-green: #17a84f;
    --ring-green: #1f9a56;
    --stripe-pink: #ec2a86;
    --stripe-red: #e91e26;
    --stripe-yellow: #fcc35c;
    --gold: #e8b24a;
    --ink: #111111;
  }
  * { margin: 0; padding: 0; box-sizing: border-box; }
  html, body {
    width: 1190px;
    height: 1200px;
    overflow: hidden;
    background: var(--backdrop);
  }
  .canvas {
    position: relative;
    width: 1190px;
    height: 1200px;
  }
  .pack-front {
    position: absolute;
    left: 295px;
    top: 125px;
    width: 600px;
    height: 950px;
    background: var(--pack-black);
  }
  .grind-band {
    position: absolute;
    left: 125px;
    top: 33px;
    width: 417px;
    height: 158px;
    background: var(--band-green);
    display: flex;
    align-items: center;
    justify-content: center;
    font-family: "Fira Sans", sans-serif;
    font-weight: 700;
    font-size: 27px;
    letter-spacing: 0.5px;
    color: var(--ink);
  }
  .brand {
    position: absolute;
    left: 0;
    top: 275px;
    width: 100%;
    display: flex;
    align-items: center;
    justify-content: center;
    gap: 16px;
  }
  .brand-dot {
    width: 34px;
    height: 34px;
    border-radius: 50%;
    background: var(--gold);
  }
  .brand-name {
    font-family: "Fira Sans", sans-serif;
    font-weight: 400;
    font-size: 30px;
    color: var(--gold);
  }
  .stripes {
    position: absolute;
    left: 58px;
    top: 375px;
    width: 475px;
    height: 575px;
  }
  .stripe { width: 100%; }
  .stripe--pink { height: 192px; background: var(--stripe-pink); }
  .stripe--red { height: 141px; background: var(--stripe-red); }
  .stripe--yellow { height: 242px; background: var(--stripe-yellow); }
  .roast-seal {
    position: absolute;
    left: 300px;
    top: 650px;
    width: 284px;
    height: 284px;
    margin: -142px 0 0 -142px;
    border-radius: 50%;
    background: var(--pack-black);
    border: 8px solid var(--ring-green);
    display: flex;
    flex-direction: column;
    align-items: center;
    justify-content: center;
    color: var(--gold);
  }
  .roast-name {
    font-family: "Fira Sans", sans-serif;
    font-weight: 600;
    font-size: 27px;
  }
  .roast-mark {
    width: 34px;
    height: 30px;
    margin: 30px 0 34px;
    background: var(--gold);
    border-radius: 6px;
  }
  .roast-notes {
    font-family: "Merienda", cursive;
    font-size: 25px;
  }
  .net-weight {
    position: absolute;
    left: 58px;
    top: 880px;
    width: 475px;
    text-align: center;
    font-family: "Fira Sans", sans-serif;
    font-size: 20px;
    color: var(--ink);
  }
</style>
</head>
<body>
<main class="canvas">
  <section class="pack-front">
    <div class="grind-band">GROUND</div>

    <div class="brand">
      <span class="brand-dot"></span>
      <span class="brand-name">Marbella Specialty Coffee</span>
    </div>

    <div class="stripes">
      <div class="stripe stripe--pink"></div>
      <div class="stripe stripe--red"></div>
      <div class="stripe stripe--yellow"></div>
    </div>

    <div class="roast-seal">
      <p class="roast-name">Mexican Roast</p>
      <div class="roast-mark" role="img" aria-label="Small gold heart pierced by an arrow"></div>
      <p class="roast-notes">Bold and smoky</p>
    </div>

    <p class="net-weight">NET WT 12 oz (340g)</p>
  </section>
</main>
</body>
</html>
```